Unique Private Wine Label for Wine Bottles (UPDATED BRIEF)

Updated Brief Oct 15, 2017. Please see below!

I am looking for a unique wine label designs for my wine bottles. I create wine and would like to have wine labels for my bottles. I am looking for a main label and then several additional labels with the same design just with the type of wine listed on the label (see below for wine types). This is private wine for family and friends to consume not commercially produced wine.

I would like a rustic, classic or vintage design with some color in the label. I do have a specific name for the wine which i like to call "Fernhollow" . I would like to see different designs.

We would like vintage or classic labels. Please give me a few multiple designs based on above. I also want to have a main label and then incorporate different types of wine into the labels like "Chardonnay" or "Pinot Noir" or "Sauvignon Blanc" or "Caberent Savignon" or "Merlot" below the name of the wine. As an example, the labels will be the same design but the word Sauvignon Blanc will be incorporated into the design for this type of wine label and so on for the other types of wine.

Please let me know if you have any questions.
Updates

Project Deadline Extended
Reason: I Have changed the vision of the design. I would like a classic, rustic or vintage design NOT a beach theme. The brief has been updated as of Oct 15, 2017. Please see updated brief for instructions on new design

Note: I have changed the vision of the design. I would like a classic, rustic or vintage design NOT a beach theme. The brief has been updated as of Oct 15, 2017. Please see updated brief for instructions on new design. I would like new designers to provide new designs! Payment is Guaranteed! Thanks!

Target Market(s)

This is private wine for family and friends to consume not commercially produced wine.

Font styles to use
Decorative
Script

Colors

Designer to choose colors to be used in the design.

Requirements
Must have
• Updated Brief Oct 15, 2017. Please see below!
• I am looking for a unique wine label designs for my wine bottles. I create wine and would like to have wine labels for my bottles. I am looking for a main label and then several additional labels with the same design just with the type of wine listed on the label (see below for wine types). This is private wine for family and friends to consume not commercially produced wine.
• I would like a rustic, classic or vintage design with some color in the label. I do have a specific name for the wine which i like to call "Fernhollow". I would like to see different designs.
• We would like vintage or classic labels. Please give me a few multiple designs based on above. I also want to have a main label and then incorporate different types of wine into the labels like "Chardonnay" or "Pinot Noir" or "Sauvignon Blanc" or "Caberent Savignon" or "Merlot" below the name of the wine. As an example, the labels will be the same design but the word Sauvignon Blanc will be incorporated into the design for this type of wine label and so on for the other types of wine.
• Please let me know if you have any questions.
Nice to have
Should not have
• Please see the updated brief instructions above. I DO NOT WANT A BEACH THEME ANYMORE!

```html
<!DOCTYPE html>
<html lang="en">
<head>
<meta charset="utf-8">
<title>Fernhollow Wine Labels</title>
<link href="https://fonts.googleapis.com/css2?family=Damion&display=swap" rel="stylesheet">
<style>
  :root {
    --backdrop: #e7e7e7;
    --ink: #111111;
    --paper: #ffffff;
    --pinot: #f5b71e;
    --merlot: #86cbc4;
    --chardonnay: #96c33f;
    --ornament: #9a9a9a;
  }
  html, body {
    margin: 0;
    padding: 0;
    width: 1200px;
    height: 1000px;
    overflow: hidden;
    background: var(--backdrop);
  }
  .label-sheet { display: block; width: 1200px; height: 1000px; }
  .label--pinot { --label-colour: var(--pinot); }
  .label--merlot { --label-colour: var(--merlot); }
  .label--chardonnay { --label-colour: var(--chardonnay); }

  .label-outline { fill: var(--paper); stroke: var(--ink); stroke-width: 7; stroke-linejoin: round; }
  .label-inner { fill: none; stroke: var(--ink); stroke-width: 2.5; }
  .panel-fill { fill: var(--label-colour); stroke: var(--ink); stroke-width: 5; }
  .panel-stripes { fill: url(#pinstripe); }
  .side-block { fill: var(--ink); }
  .side-hatch { stroke: var(--paper); stroke-width: 3; }
  .name-band { fill: var(--paper); stroke: var(--ink); stroke-width: 10; }
  .ornament-area { fill: var(--ornament); }
  .banner { fill: var(--paper); stroke: var(--ink); stroke-width: 4; }
  .seal { fill: var(--paper); stroke: var(--ink); stroke-width: 5; }
  .seal-line { stroke: var(--ink); stroke-width: 2; }

  .wine-name { font-family: 'Damion', cursive; font-size: 70px; fill: var(--ink); }
  .variety, .volume {
    font-family: 'Damion', cursive;
    font-size: 32px;
    fill: var(--label-colour);
    stroke: var(--ink);
    stroke-width: 0.7;
  }
  .seal-text { font-family: 'Damion', cursive; font-size: 19px; fill: var(--ink); }
  .seal-name { font-family: 'Damion', cursive; font-size: 10px; fill: var(--ink); }
</style>
</head>
<body>
<svg class="label-sheet" viewBox="0 0 1200 1000" xmlns="http://www.w3.org/2000/svg">
  <defs>
    <pattern id="pinstripe" width="8" height="10" patternUnits="userSpaceOnUse">
      <rect x="5" y="0" width="2" height="10" fill="#ffffff" fill-opacity="0.5"/>
    </pattern>
    <g id="label-body">
      <path class="label-outline" d="M45,75 A146 146 0 0 1 300,75 L300,160 L345,160 L345,575 L300,575 L300,645 A146 146 0 0 1 45,645 L45,575 L0,575 L0,160 L45,160 Z"/>
      <path class="label-inner" d="M57,80 A134 134 0 0 1 288,80 M57,640 A134 134 0 0 0 288,640"/>

      <rect class="ornament-area" x="110" y="42" width="125" height="56" rx="10" role="img" aria-label="Scrollwork ornament"/>
      <rect class="ornament-area" x="110" y="620" width="125" height="50" rx="10" role="img" aria-label="Scrollwork ornament"/>

      <rect class="side-block" x="2" y="162" width="36" height="128"/>
      <rect class="side-block" x="307" y="162" width="36" height="128"/>
      <rect class="side-block" x="2" y="430" width="36" height="143"/>
      <rect class="side-block" x="307" y="430" width="36" height="143"/>
      <g class="side-hatch">
        <line x1="2" y1="195" x2="38" y2="195"/><line x1="2" y1="225" x2="38" y2="225"/><line x1="2" y1="255" x2="38" y2="255"/>
        <line x1="307" y1="195" x2="343" y2="195"/><line x1="307" y1="225" x2="343" y2="225"/><line x1="307" y1="255" x2="343" y2="255"/>
        <line x1="2" y1="465" x2="38" y2="465"/><line x1="2" y1="500" x2="38" y2="500"/><line x1="2" y1="535" x2="38" y2="535"/>
        <line x1="307" y1="465" x2="343" y2="465"/><line x1="307" y1="500" x2="343" y2="500"/><line x1="307" y1="535" x2="343" y2="535"/>
      </g>

      <rect class="panel-fill" x="38" y="115" width="269" height="175"/>
      <rect class="panel-stripes" x="40" y="117" width="265" height="171"/>
      <rect class="panel-fill" x="38" y="430" width="269" height="175"/>
      <rect class="panel-stripes" x="40" y="432" width="265" height="171"/>

      <rect class="name-band" x="3" y="290" width="339" height="140"/>

      <rect class="banner" x="70" y="200" width="205" height="52" rx="12"/>
      <rect class="banner" x="70" y="468" width="205" height="52" rx="12"/>

      <circle class="seal" cx="172" cy="160" r="28"/>
      <text class="seal-name" x="172" y="164" text-anchor="middle">Fernhollow</text>
      <circle class="seal" cx="172" cy="563" r="28"/>
      <line class="seal-line" x1="148" y1="548" x2="196" y2="548"/>
      <line class="seal-line" x1="148" y1="578" x2="196" y2="578"/>
      <text class="seal-text" x="172" y="570" text-anchor="middle">2017</text>

      <text class="wine-name" x="172" y="383" text-anchor="middle">Fernhollow</text>
      <text class="volume" x="172" y="505" text-anchor="middle">750 ml</text>
    </g>
  </defs>

  <g class="label label--pinot" transform="translate(50,118)">
    <use href="#label-body"/>
    <text class="variety" x="172" y="237" text-anchor="middle">Pinot Noir</text>
  </g>

  <g class="label label--merlot" transform="translate(290,118)">
    <use href="#label-body"/>
    <text class="variety" x="172" y="237" text-anchor="middle">Merlot</text>
  </g>

  <g class="label label--chardonnay" transform="translate(590,118)">
    <use href="#label-body"/>
    <text class="variety" x="172" y="237" text-anchor="middle">Chardonnay</text>
  </g>
</svg>
</body>
</html>
```